Designs of screens for job search mobile app

Design the following screens:

1. Login
2. Job search results in tabs
3. Job details in cards format
4. Profile
5. Settings

Logo and references are provided. The app need to be playful, easy to use, different from traditional job search app like Hirevo, Workbrix and others and targeted to Millennial users (age 18-30).

The main app reference is Pogura, in terms of the colorful and fun color and font scheme.

Target Market(s)

Millennial users (age 18-30).

Requirements
Must have
• A fun, playful feel

```html
<!DOCTYPE html>
<html lang="en">
<head>
<meta charset="utf-8">
<title>Settings</title>
<link rel="stylesheet" href="https://fonts.googleapis.com/css2?family=Montserrat:wght@500;600;700&display=swap">
<style>
  :root{
    --bg:#f7f6f6;
    --screen:#ffffff;
    --ink:#1d1d1f;
    --teal:#14b3ad;
    --line:#ececec;
    --muted:#c4c4c4;
    --tabbar:#f8f8f8;
  }
  *{box-sizing:border-box;margin:0;padding:0}
  html,body{width:1200px;height:1200px;overflow:hidden;background:var(--bg)}
  body{font-family:"Montserrat",Arial,sans-serif;color:var(--ink);position:relative}
  .screen{position:absolute;left:280px;top:38px;width:640px;height:1124px;background:var(--screen);overflow:hidden;box-shadow:0 0 0 1px #e4e4e4}
  .status-bar{position:absolute;top:0;left:0;right:0;height:36px;display:flex;align-items:center;justify-content:space-between;padding:0 16px;font-size:17px;font-weight:500}
  .status-left{display:flex;align-items:center;gap:8px}
  .signal{display:flex;gap:3px}
  .signal i{width:9px;height:9px;border-radius:50%;border:1.5px solid var(--ink)}
  .signal i.on{background:var(--ink)}
  .status-right{display:flex;align-items:center;gap:6px}
  .battery{width:26px;height:12px;border:1.5px solid var(--ink);border-radius:3px;padding:1.5px;position:relative}
  .battery::after{content:"";position:absolute;right:-4px;top:3px;width:2px;height:4px;background:var(--ink)}
  .battery span{display:block;width:100%;height:100%;background:var(--ink);border-radius:1px}
  .status-time{position:absolute;left:0;right:0;text-align:center;pointer-events:none}
  .title{position:absolute;top:52px;left:0;right:0;text-align:center;font-size:24px;font-weight:600}
  .divider{position:absolute;left:24px;right:32px;height:2px;background:var(--line)}
  .section-title{position:absolute;left:26px;top:130px;font-size:26px;font-weight:600}
  .row{position:absolute;left:24px;right:32px;height:40px;display:flex;align-items:center;color:var(--teal);font-size:20px;font-weight:600}
  .row svg{width:28px;height:28px;margin-left:6px;margin-right:14px;flex:none}
  .row .dot{width:22px;height:22px;border:2.4px solid var(--teal);border-radius:50%;margin-left:9px;margin-right:17px;flex:none}
  .toggle{margin-left:auto;width:70px;height:32px;border:3px solid var(--teal);border-radius:16px;position:relative}
  .toggle::after{content:"";position:absolute;right:7px;top:6px;width:15px;height:15px;border-radius:50%;background:var(--teal)}
  .tab-bar{position:absolute;left:0;right:0;bottom:0;height:90px;background:linear-gradient(#fbfbfb,#f3f3f3);border-top:1px solid #eee;display:flex;justify-content:space-around;align-items:center;padding:0 40px}
  .tab-bar svg{width:42px;height:42px;fill:none;stroke:var(--muted);stroke-width:2;stroke-linejoin:round;stroke-linecap:round}
  .tab-bar .active svg{stroke:var(--teal)}
</style>
</head>
<body>
<main class="screen">
  <header class="status-bar">
    <div class="status-left">
      <div class="signal"><i class="on"></i><i class="on"></i><i class="on"></i><i></i><i></i></div>
      <span>NOVA</span>
      <svg width="20" height="15" viewBox="0 0 20 15"><path d="M1 5a13 13 0 0 1 18 0M4 8.5a8.5 8.5 0 0 1 12 0M7 12a4 4 0 0 1 6 0" fill="none" stroke="#1d1d1f" stroke-width="2" stroke-linecap="round"/></svg>
    </div>
    <span class="status-time">4:21 PM</span>
    <div class="status-right"><span>100%</span><div class="battery"><span></span></div></div>
  </header>

  <h1 class="title">Settings</h1>
  <div class="divider" style="top:103px"></div>

  <h2 class="section-title">Notifications</h2>
  <div class="divider" style="top:183px"></div>

  <div class="row" style="top:196px">
    <svg viewBox="0 0 24 24" fill="none" stroke="currentColor" stroke-width="1.6" stroke-linejoin="round"><path d="M3 5h18v11H9l-4 3v-3H3z"/><path d="M7 9h10M7 12h7"/></svg>
    Job Messages<span class="toggle"></span>
  </div>
  <div class="divider" style="top:249px"></div>
  <div class="row" style="top:264px">
    <svg viewBox="0 0 24 24" fill="none" stroke="currentColor" stroke-width="1.6" stroke-linejoin="round"><rect x="3" y="6" width="18" height="12"/><path d="M3 6l9 7 9-7"/></svg>
    Send Notification by Email Too<span class="toggle"></span>
  </div>
  <div class="divider" style="top:319px"></div>

  <div class="divider" style="top:357px"></div>
  <div class="row" style="top:370px"><span class="dot"></span>Like Us on Friendora</div>
  <div class="divider" style="top:425px"></div>
  <div class="row" style="top:438px">
    <svg viewBox="0 0 24 24" fill="none" stroke="currentColor" stroke-width="1.6"><circle cx="18" cy="5.5" r="2.5"/><circle cx="6" cy="12" r="2.5"/><circle cx="18" cy="18.5" r="2.5"/><path d="M8.2 10.8l7.6-4M8.2 13.2l7.6 4"/></svg>
    Share on Workbrix
  </div>
  <div class="divider" style="top:495px"></div>
  <div class="row" style="top:510px"><span class="dot"></span>Follow on Chirply</div>
  <div class="divider" style="top:565px"></div>
  <div class="row" style="top:584px">
    <svg viewBox="0 0 24 24" fill="none" stroke="currentColor" stroke-width="1.6" stroke-linejoin="round"><path d="M12 3l2.7 5.6 6.1.8-4.5 4.2 1.1 6.1L12 16.8l-5.4 2.9 1.1-6.1-4.5-4.2 6.1-.8z"/></svg>
    Rate Us on Appvault
  </div>
  <div class="divider" style="top:639px"></div>

  <div class="divider" style="top:677px"></div>
  <div class="row" style="top:690px">
    <svg viewBox="0 0 24 24" fill="none" stroke="currentColor" stroke-width="1.6" stroke-linecap="round"><circle cx="12" cy="12" r="8.5"/><path d="M9.6 9.6a2.5 2.5 0 1 1 3.4 2.3c-.7.3-1 .8-1 1.5v.4"/><circle cx="12" cy="16.6" r=".4"/></svg>
    Help
  </div>
  <div class="divider" style="top:745px"></div>
  <div class="row" style="top:758px">
    <svg viewBox="0 0 24 24" fill="none" stroke="currentColor" stroke-width="1.6" stroke-linejoin="round"><rect x="5" y="11" width="14" height="10" rx="1"/><path d="M8 11V8a4 4 0 0 1 8 0v3"/><circle cx="12" cy="16" r="1"/></svg>
    Privacy Policy
  </div>
  <div class="divider" style="top:813px"></div>
  <div class="row" style="top:830px">
    <svg viewBox="0 0 24 24" fill="none" stroke="currentColor" stroke-width="1.6" stroke-linejoin="round"><path d="M5 3h11l3 3v15H5z"/><path d="M8 8h8M8 11h8M8 14h8M8 17h5"/></svg>
    Terms of Use
  </div>
  <div class="divider" style="top:885px"></div>

  <nav class="tab-bar">
    <span class="tab"><svg viewBox="0 0 24 24"><path d="M3 11l9-7.5 9 7.5M5.5 9v11.5h5v-6h3v6h5V9"/></svg></span>
    <span class="tab"><svg viewBox="0 0 24 24"><circle cx="14" cy="10" r="6"/><path d="M9.8 14.2L4 20M14 7v3h2.5"/></svg></span>
    <span class="tab"><svg viewBox="0 0 24 24"><rect x="3" y="7" width="18" height="13" rx="1"/><path d="M9 7V4.5h6V7M7 7v13M17 7v13"/></svg></span>
    <span class="tab"><svg viewBox="0 0 24 24"><rect x="5.5" y="3" width="13" height="18" rx="1"/><path d="M9 8h6M9 12h6M9 16h6"/></svg></span>
    <span class="tab active"><svg viewBox="0 0 24 24"><circle cx="12" cy="12" r="3"/><path d="M10.3 3h3.4l.5 2.6 1.8 1 2.5-.9 1.7 2.9-2 1.8v2.1l2 1.8-1.7 2.9-2.5-.9-1.8 1-.5 2.6h-3.4l-.5-2.6-1.8-1-2.5.9-1.7-2.9 2-1.8v-2.1l-2-1.8 1.7-2.9 2.5.9 1.8-1z"/></svg></span>
  </nav>
</main>
</body>
</html>
```